Site for company producing and selling products for children's health

We need an appealing professional web site design and images for a brand new company producing and selling products focused on children’s health. The site will offer information to visitors on the company, the company’s products, and general resources related to children’s health. Additionally the site will offer e-commerce functionality to allow for ordering of the company’s products.
The content and navigation for the site will be generated by programming, such as php or asp, and therefore any images used in the navigation portions of the site should allow for HTML markup to be overlaid rather than having the text built into the image or graphic.
The design must include 2 layouts, one for the landing/home page that includes only top navigation, and an inner page layout that includes both top and left navigation.
The header area of the site should include a place for links to access the visitor’s cart and profile similar to the top sections of plumvat.com, tidelor.com, and keenmart.com.
The landing page of the site should include some type of “changing” image area where we can include multiple image files for rotation to visitors similar to what is seen at vorta.com or brisksip.com. The flash/animation mechanism does not need to be provided (although it would be a plus if it was) but the design must accommodate the space for it.
The company’s colors are Orange (FF9900) and Blue (0066FF) and the logo can be viewed at http://wonkibrook.com/logo.png
All CSS and markup provided must be display consistently in Internet Explorer 7+, FifeFox, Google Chrome, and Safari.
Incorporating social media links (facebook, twitter, etc.) is desirable.
Parents who are conscious of health risks associated with children's diets and consumer food products.
E-Commerce

```html
<!DOCTYPE html>
<html lang="en">
<head>
<meta charset="utf-8">
<title>Wonkibrook — Children's Health</title>
<link rel="stylesheet" href="https://fonts.googleapis.com/css2?family=Ubuntu:wght@400;500;700&family=Arimo:wght@400;700&family=Archivo+Black&family=Fjalla+One&display=swap">
<style>
:root{
  --orange:#ff9900;
  --orange-deep:#ee6a10;
  --blue:#0066ff;
  --blue-dark:#0a4fd6;
  --navy:#0b2a6e;
  --red:#e5141b;
  --panel:#ececec;
  --page:#f3f3f3;
  --ink:#111;
  --footer-top:#5b6a92;
  --footer-bottom:#38456b;
}
*{box-sizing:border-box;margin:0;padding:0}
html,body{width:1200px;height:974px;overflow:hidden}
body{background:var(--page);font-family:"Arimo",Arial,sans-serif;color:var(--ink);position:relative}
a{color:inherit;text-decoration:none}

.topbar{position:absolute;left:12px;top:0;width:1180px;height:52px;border-radius:0 0 10px 10px;
  background:linear-gradient(#7fb0ff 0%,#2c7cff 45%,#0a5cf0 100%);box-shadow:0 3px 5px rgba(0,0,0,.35)}
.topnav{position:absolute;left:31px;top:0;height:48px;display:flex;align-items:center;gap:19px;
  font-family:"Ubuntu",sans-serif;font-weight:700;font-size:13px;color:#fff}
.shop-btn{position:absolute;left:956px;top:10px;width:205px;height:28px;border-radius:5px;border:1px solid #7a4a00;
  background:linear-gradient(#ffc04a,var(--orange));font-family:"Arimo",sans-serif;font-weight:700;font-size:13px;
  display:flex;align-items:center;justify-content:center;gap:14px;color:#111}
.shop-btn svg{width:18px;height:18px}

.brand{position:absolute;left:64px;top:142px;display:flex;align-items:center;gap:10px;
  font-family:"Ubuntu",sans-serif;font-weight:700;font-size:29px;color:var(--blue)}
.brand-dot{width:26px;height:26px;border-radius:50%;background:var(--orange)}
.site-title{position:absolute;left:461px;top:90px;font-family:"Archivo Black",sans-serif;font-size:72px;
  color:var(--orange-deep);letter-spacing:.5px}

.hero{position:absolute;left:12px;top:224px;width:1178px;height:410px;background:var(--panel);border-radius:8px}
.hero-slide{position:absolute;left:19px;top:47px;width:658px;height:349px;
  background:linear-gradient(180deg,#9fc6ec 0%,#cfdcd6 30%,#e9dccb 55%,#e3a98a 80%,#e8a0a8 100%)}
.welcome{position:absolute;left:708px;top:50px;width:440px}
.welcome h1{font-weight:400;font-size:26px;line-height:44px}
.welcome h1 span{font-size:36px;color:var(--orange)}
.welcome p{margin-top:14px;font-size:14.3px;line-height:20.5px;width:428px}
.welcome p + p{margin-top:20px}
.read-more{position:absolute;left:709px;top:356px;width:161px;height:41px;background:var(--blue);color:#fff;
  font-size:19px;display:flex;align-items:center;padding-left:13px;gap:14px}
.read-more svg{width:22px;height:12px}

.ticker{position:absolute;left:13px;top:653px;width:1178px;height:68px;border:1px solid #8cb4d0;
  background:linear-gradient(#e6f1fa,#b7d6ee)}
.pager-btn{position:absolute;top:18px;width:107px;height:32px;border-radius:5px;border:1px solid #c06a00;
  background:linear-gradient(#ffc15a,#ff9a1a);font-weight:700;font-size:14px;color:#111;
  display:flex;align-items:center;justify-content:center;gap:10px}
.pager-btn svg{width:17px;height:17px}
.pager-btn.prev{left:10px}
.pager-btn.next{left:597px}
.ticker-text{position:absolute;left:126px;top:21px;font-family:"Ubuntu",sans-serif;font-size:18.5px;color:var(--navy)}
.follow{position:absolute;left:737px;top:14px;font-family:"Fjalla One",sans-serif;font-size:27px;color:var(--red)}
.social{position:absolute;top:17px;width:34px;height:34px;border-radius:50%;
  background:radial-gradient(circle at 40% 35%,#6fa4e6,#1f4f9a);box-shadow:0 2px 3px rgba(0,0,0,.35)}
.social.one{left:884px}.social.two{left:958px;background:radial-gradient(circle at 40% 35%,#bfe9ff,#3fa6dc)}.social.three{left:1032px}

.feature{position:absolute;top:733px;width:286px;height:158px;border:1px solid #c7852b;overflow:hidden}
.feature.care{left:13px;background:linear-gradient(120deg,#f4f1ec,#e6cdb8 55%,#f7f3ee)}
.feature.food{left:311px;background:linear-gradient(100deg,#d9dee4,#f0d6c2 55%,#f1e4d8)}
.feature.doctor{left:608px;background:linear-gradient(100deg,#f3e2cc,#ecd3c3 45%,#dfe4e8)}
.feature-title{position:absolute;font-family:"Fjalla One",sans-serif}
.care .feature-title{right:8px;top:4px;font-family:"Arimo",sans-serif;font-size:34px;color:var(--red);text-align:right;line-height:36px}
.care .feature-title small{display:block;font-size:13px;font-weight:700;color:#111;line-height:14px}
.food .feature-title{left:29px;bottom:5px;font-size:22.5px;color:var(--blue)}
.doctor .feature-title{right:12px;bottom:6px;font-size:27px;line-height:29px;color:var(--red);text-align:center}

.newsletter{position:absolute;left:906px;top:733px;width:285px;height:158px;border:1px solid #c9941a;
  background:linear-gradient(#fff0a0,#ffc42e);padding:14px 13px}
.newsletter h2{font-family:"Fjalla One",sans-serif;font-weight:400;font-size:20.5px;color:#1a1a1a}
.field{display:block;margin-top:10px;width:235px;height:20px;border:0;background:#ececec;padding-left:4px;
  font-family:"Arimo",sans-serif;font-size:12px;color:#666}
.field:first-of-type{margin-top:11px}
.submit{display:block;margin-top:12px;width:86px;height:32px;border:1px solid #1b3d9a;
  background:linear-gradient(#5c9cff,var(--blue-dark));color:#fff;font-size:20px;font-family:"Arimo",sans-serif}

.footer{position:absolute;left:13px;top:906px;width:1178px;height:68px;
  background:linear-gradient(var(--footer-top),var(--footer-bottom));color:#fff;text-align:center;
  font-family:"Ubuntu",sans-serif;font-size:13px}
.footer nav{display:flex;justify-content:center;gap:16px;margin-top:15px}
.footer p{margin-top:6px}
</style>
</head>
<body>

<header class="topbar">
  <nav class="topnav">
    <a href="#">Home</a><a href="#">Latest News</a><a href="#">About Us</a><a href="#">Services</a><a href="#">Product Page</a><a href="#">Contact Us</a>
  </nav>
  <a class="shop-btn" href="#">SHOP BY CATEGORY
    <svg viewBox="0 0 18 18"><rect x="1" y="1" width="16" height="16" rx="3" fill="#fff" opacity=".85"/><path d="M7 5l4 4-4 4" stroke="#e07a00" stroke-width="2.2" fill="none"/></svg>
  </a>
</header>

<div class="brand"><span class="brand-dot"></span>wonkibrook</div>
<div class="site-title">Wonkibrook</div>

<section class="hero">
  <div class="hero-slide" role="img" aria-label="Rotating banner photo: a family sharing a meal at an outdoor table"></div>
  <div class="welcome">
    <h1>welcome to <span>Wonkibrook</span></h1>
    <p>Lorem Ipsum is simply dummy text of the printing and typesetting industry. Lorem Ipsum has been the industry's standard dummy text ever since the 1500s, when an unknown printer took a galley of type and scrambled it to make a type specimen book. It has survived not only five centuries, but also the leap into electronic typesetting, remaining essentially unchanged.</p>
    <p>It was popularised in the 1960s with the release of Letraset sheets containing Lorem Ipsum passages, and more recently with desktop publishing software like Aldus PageMaker including versions of Lorem Ipsum.</p>
  </div>
  <a class="read-more" href="#">Read More
    <svg viewBox="0 0 22 12"><path d="M2 2l4 4-4 4M10 2l4 4-4 4" stroke="#fff" stroke-width="2" fill="none"/></svg>
  </a>
</section>

<section class="ticker">
  <a class="pager-btn prev" href="#"><svg viewBox="0 0 17 17"><rect x="1" y="1" width="15" height="15" rx="3" fill="#fff" opacity=".85"/><path d="M10 4l-4 4.5 4 4.5" stroke="#e07a00" stroke-width="2" fill="none"/></svg>Previous</a>
  <div class="ticker-text">Lorem ipsum dolo sit amet nuno valencia estat di morea</div>
  <a class="pager-btn next" href="#">Next<svg viewBox="0 0 17 17"><rect x="1" y="1" width="15" height="15" rx="3" fill="#fff" opacity=".85"/><path d="M7 4l4 4.5-4 4.5" stroke="#e07a00" stroke-width="2" fill="none"/></svg></a>
  <div class="follow">Follow us on</div>
  <a class="social one" href="#" aria-label="Social link"></a>
  <a class="social two" href="#" aria-label="Social link"></a>
  <a class="social three" href="#" aria-label="Social link"></a>
</section>

<a class="feature care" href="#" role="img" aria-label="Photo of a baby in a flower headband crawling">
  <div class="feature-title">Baby Care<small>Read More</small></div>
</a>
<a class="feature food" href="#" role="img" aria-label="Photo of a baby drinking from a bottle">
  <div class="feature-title">BEST FOODS FOR YOUR CHILD</div>
</a>
<a class="feature doctor" href="#" role="img" aria-label="Photo of a young girl with a doctor">
  <div class="feature-title">Doctors<br>Chamber</div>
</a>

<form class="newsletter">
  <h2>SUBSCRIBE OUR NEWSLETTER</h2>
  <input class="field" type="text" placeholder="Your Name">
  <input class="field" type="text" placeholder="Your Email Id">
  <button class="submit" type="button">Submit</button>
</form>

<footer class="footer">
  <nav><a href="#">Home</a><a href="#">Latest News</a><a href="#">About Us</a><a href="#">Services</a><a href="#">Product Page</a><a href="#">Contact Us</a></nav>
  <p>© Copyright &nbsp; | &nbsp; All Rights Reserved</p>
</footer>

</body>
</html>
```